Website for CIO outsourcing company
Velmont Systems, LLC
Website for CIO outsourcing company - Information Technology
Creative Brief
Information Technology
www.govelmontexample.com
Velmont knows that IT plays a central role to each business, and can be a determining factor in the success or failure of that business. As a committed partner we are looking for the right balance between user experience and employee satisfaction, and achieve this through care, communication and sustainable solutions. To accomplish this Velmont works closely with our clients to offer the best IT solutions to support their business processes.
Services: IT Automation: Outsourcing Project Services 360 degree Consultation & Review Need plain square, plain square and plain square integration. Font: Linux Libertine
Modern
Colors that work with logo
left side
www.brandeko.example.co.uk
www.plexorvanta.example.nl
www.hwtnet.example.net
Content-wise (translation to English) www.dorvenkaal-ict.example.nl/ is the site that has the kind of verbiage we are looking for.

```html
<!DOCTYPE html>
<html lang="en">
<head>
<meta charset="utf-8">
<title>Velmont Systems, LLC – CIO outsourcing company</title>
<link href="https://fonts.googleapis.com/css2?family=Crimson+Pro:wght@400;600;700&family=Tinos:wght@400;700&display=swap" rel="stylesheet">
<style>
:root{
  --red:#c8202a;
  --red-dark:#9e151d;
  --ink:#222;
  --text:#555;
  --muted:#888;
  --line:#dcdcdc;
  --bg:#f4f4f4;
  --nav-bg:#f0f0f0;
  --footer:#5a5a5a;
  --footer-dark:#4a4a4a;
}
*{box-sizing:border-box;margin:0;padding:0}
html,body{width:1200px;height:840px;overflow:hidden}
body{background:linear-gradient(#fff 0,#fafafa 400px,var(--bg) 760px);font-family:"Tinos",serif;color:var(--text);position:relative}
a{color:inherit;text-decoration:none}
.wrap{position:absolute;left:173px;width:860px}

/* header */
.site-header{top:0;height:70px}
.brand{position:absolute;left:8px;top:16px;display:flex;align-items:center;gap:10px}
.brand-mark{width:26px;height:26px;background:var(--red)}
.brand-name{font-family:"Crimson Pro",serif;font-weight:700;font-size:34px;color:var(--red);letter-spacing:1px}
.login{position:absolute;right:0;top:22px;display:flex;gap:8px;align-items:center}
.login input{width:140px;height:20px;border:1px solid #cfcfcf;background:#fff;font:11px "Tinos",serif;padding:0 5px;color:var(--muted)}
.login-btn{width:58px;height:20px;background:linear-gradient(#555,#2e2e2e);color:#fff;font-size:11px;display:flex;align-items:center;justify-content:center;border-radius:2px}
.forgot{position:absolute;left:507px;top:46px;font-size:11px;color:var(--red)}

/* nav */
.main-nav{top:73px;height:34px;background:var(--nav-bg);border-top:1px solid var(--line);border-bottom:1px solid var(--line);display:flex;align-items:center}
.main-nav ul{list-style:none;display:flex;height:100%}
.main-nav li{font-size:11px;color:#666;padding:0 14px;display:flex;align-items:center;border-right:1px solid var(--line)}
.main-nav li.active{color:var(--red);background:#fff}
.search{margin-left:auto;margin-right:34px;width:192px;height:22px;background:#fff;border:1px solid #d2d2d2;display:flex;align-items:center;justify-content:space-between;padding:0 6px;font-size:10px;color:var(--muted)}

/* services */
.services{top:132px;width:256px;height:270px;list-style:none}
.service{display:flex;gap:12px;height:66px;padding-top:6px;border-bottom:1px solid #e6e6e6}
.service:last-child{border-bottom:0}
.service-icon{flex:none;width:38px;height:38px;border-radius:5px;background:linear-gradient(#e0403a,var(--red-dark));display:flex;align-items:center;justify-content:center}
.service h3{font-family:"Crimson Pro",serif;font-weight:400;font-size:19px;line-height:17px;color:var(--ink);white-space:nowrap;letter-spacing:-.2px}
.service p{font-size:10px;line-height:12px;color:var(--text);margin-top:3px}
.service p em{font-style:normal;color:var(--red)}

/* slider */
.slider{position:absolute;left:432px;top:124px;width:595px;height:276px;background:linear-gradient(120deg,#3a4048 0%,#6e7781 35%,#c9ccd0 65%,#eef0f2 100%);overflow:hidden}
.slider-bar{position:absolute;left:0;top:0;right:0;height:38px;background:rgba(90,90,90,.55);display:flex;align-items:center;justify-content:space-between;padding:0 10px}
.slider-bar h2{font-family:"Crimson Pro",serif;font-weight:400;font-size:28px;color:#fff}
.slider-arrows{display:flex;gap:3px}

/* sections */
.section-title{font-size:13px;color:var(--ink);letter-spacing:.5px;height:28px;display:flex;align-items:center;border-bottom:1px solid var(--line)}
.expertise{top:420px;width:632px}
.expertise-photo{position:absolute;left:0;top:36px;width:276px;height:122px;background:linear-gradient(90deg,#2b3a42,#7d8c8f 50%,#3c4a52)}
.expertise-text{position:absolute;left:296px;top:36px;width:336px}
.expertise-text h3{font-family:"Crimson Pro",serif;font-weight:600;font-size:17px;line-height:18px;color:var(--ink)}
.expertise-text p{font-size:11px;line-height:13px;margin-top:8px}
.expertise-text p a{color:var(--red)}

.news{top:420px;left:823px;width:210px}
.news-item{font-size:10px;line-height:12px;padding:8px 0 6px;border-bottom:1px solid #e6e6e6}
.news-item strong{display:block;color:var(--ink);margin:4px 0}
.news-item a{color:var(--red)}

.partners{top:648px;width:632px}
.partner-band{margin-top:10px;height:58px;background:linear-gradient(#fff,#e9e9e9);border:1px solid #e0e0e0;display:flex;align-items:center;justify-content:space-around;padding:0 10px}
.badge{height:26px;border-radius:3px}

.contact{top:648px;left:823px;width:210px;font-size:11px;line-height:13px}
.contact p{margin-top:8px}
.contact a{color:var(--red)}

/* footer */
.site-footer{position:absolute;left:0;top:766px;width:1200px;height:74px;background:linear-gradient(var(--footer),var(--footer-dark))}
.footer-nav{position:absolute;left:173px;top:22px;font-size:10px;color:#eee;display:flex;gap:6px}
.copyright{position:absolute;left:173px;top:40px;font-size:9px;color:#bbb}
.follow{position:absolute;left:823px;top:16px;display:flex;align-items:center;gap:8px;font-size:10px;color:#eee}
.social{width:32px;height:32px;border-radius:4px}
</style>
</head>
<body>

<header class="wrap site-header">
  <div class="brand"><span class="brand-mark"></span><span class="brand-name">VELMONT</span></div>
  <form class="login">
    <input type="text" value="Uname" aria-label="Username">
    <input type="text" value="Password" aria-label="Password">
    <span class="login-btn">LOGIN</span>
  </form>
  <a class="forgot" href="#">Forgot Password!</a>
</header>

<nav class="wrap main-nav">
  <ul>
    <li class="active">HOME</li><li>ABOUT US</li><li>SERVICES</li><li>EXPERTISE</li><li>CUSTOMER PORTAL</li><li>NEWS</li><li>CONTACT US</li>
  </ul>
  <div class="search">enter your email address
    <svg width="11" height="11" viewBox="0 0 12 12"><circle cx="5" cy="5" r="3.6" fill="none" stroke="#666" stroke-width="1.5"/><line x1="7.6" y1="7.6" x2="11" y2="11" stroke="#666" stroke-width="1.8"/></svg>
  </div>
</nav>

<ul class="wrap services">
  <li class="service">
    <span class="service-icon"><svg width="20" height="20" viewBox="0 0 20 20"><circle cx="10" cy="10" r="6" fill="none" stroke="#fff" stroke-width="3"/></svg></span>
    <div><h3>IT Automation</h3><p>Lorem ipsum dolor sit amet, consectetur adipiscing <em>elit sed.</em></p></div>
  </li>
  <li class="service">
    <span class="service-icon"><svg width="20" height="20" viewBox="0 0 20 20"><path d="M4 10a6 6 0 0 1 11-3M16 10a6 6 0 0 1-11 3" fill="none" stroke="#fff" stroke-width="2.4"/></svg></span>
    <div><h3>Outsourcing</h3><p>Lorem ipsum dolor sit amet, consectetur adipiscing <em>elit sed.</em></p></div>
  </li>
  <li class="service">
    <span class="service-icon"><svg width="20" height="20" viewBox="0 0 20 20"><path d="M4 4l12 12M16 4L4 16" stroke="#fff" stroke-width="3"/></svg></span>
    <div><h3>Project Services</h3><p>Lorem ipsum dolor sit amet, consectetur adipiscing <em>elit sed.</em></p></div>
  </li>
  <li class="service">
    <span class="service-icon"><svg width="20" height="20" viewBox="0 0 20 20"><rect x="3" y="3" width="14" height="14" fill="none" stroke="#fff" stroke-width="2.4"/><path d="M6 11l3 3 5-7" fill="none" stroke="#fff" stroke-width="2"/></svg></span>
    <div><h3>360 Degress Consultation<br>&amp; Review</h3><p>Lorem ipsum dolor sit amet, consectetur adipiscing <em>elit sed.</em></p></div>
  </li>
</ul>

<section class="slider" role="img" aria-label="Tablet and smartphone showing business reports on a desk with a coffee cup and charts">
  <div class="slider-bar">
    <h2>CIO outsourcing company</h2>
    <span class="slider-arrows">
      <svg width="7" height="10" viewBox="0 0 7 10"><path d="M6 0L0 5l6 5z" fill="#fff"/></svg>
      <svg width="7" height="10" viewBox="0 0 7 10"><path d="M1 0l6 5-6 5z" fill="#fff"/></svg>
    </span>
  </div>
</section>

<section class="wrap expertise">
  <h2 class="section-title">EXPERTISE</h2>
  <div class="expertise-photo" role="img" aria-label="Technician working at server racks in a data centre"></div>
  <div class="expertise-text">
    <h3>Neque porro quisquam est qui dolorem ipsum quia dolor sit amet...</h3>
    <p>Lorem ipsum dolor sit amet, consectetur adipiscing elit, sed do eiusmod tempor incididunt ut labore et dolore magna aliqua. Ut enim ad minim veniam, quis nostrud exercitation ullamco laboris nisi ut aliquip ex ea <a href="#">commodo consequat..</a></p>
  </div>
</section>

<section class="wrap news">
  <h2 class="section-title">VELMONT NEWS</h2>
  <article class="news-item">20th March, 2013<strong>Lorem ipsum dolor sit amet, consectetur adipiscing elit, sed do eiusmod tempor</strong></article>
  <article class="news-item">Lorem ipsum dolor sit amet, consectetur adipiscing elit, sed do eiusmod tempor incididunt ut labore et dolore magna aliqua. Ut enim ad minim veniam ... <a href="#">read more</a></article>
</section>

<section class="wrap partners">
  <h2 class="section-title" style="border:0;height:20px">PARTNERS</h2>
  <div class="partner-band">
    <span class="badge" style="width:120px;background:#2a5d9f"></span>
    <span class="badge" style="width:120px;background:#3b6fb5"></span>
    <span class="badge" style="width:120px;background:#d4202a"></span>
    <span class="badge" style="width:100px;background:#27418c"></span>
  </div>
</section>

<section class="wrap contact">
  <h2 class="section-title" style="border:0;height:20px">CONTACT</h2>
  <p>Lorem ipsum dolor sit amet, consectetur,<br>Ipsum 20034</p>
  <p>Phone: 555.014.2290<br>Email: <a href="#">info@govelmontexample.com</a></p>
</section>

<footer class="site-footer">
  <nav class="footer-nav"><span>HOME</span>|<span>ABOUT US</span>|<span>SERVICES</span>|<span>EXPERTISE</span>|<span>CUSTOMER PORTAL</span>|<span>NEWS</span>|<span>CONTACT US</span></nav>
  <p class="copyright">copyright © 2013 www.govelmontexample.com. All Rights Reserved</p>
  <div class="follow">FOLLOW US ON
    <span class="social" style="background:#3b5b99"></span>
    <span class="social" style="background:#2fa9e0"></span>
    <span class="social" style="background:#1f7bb6"></span>
  </div>
</footer>

</body>
</html>
```